Mendwise Partners
Project: Mendwise Partners
Mendwise Partners - Financial Services
Creative Brief
Professional
Karl Varner
Hillcrest Office Park 47 Bloem Street Kestrel Building Northbrook 2190
karl.varner@mendwisepartners-example.co.za
www.mendwisepartners-example.co.za
Try and use both the colour and black & white logos on the back.

```html
<!DOCTYPE html>
<html lang="en">
<head>
<meta charset="UTF-8">
<title>Mendwise Partners – Business Card</title>
<link rel="stylesheet" href="https://fonts.googleapis.com/css2?family=Montserrat:wght@400;500;600;700&display=swap">
<style>
  :root {
    --bg: #c9cacc;
    --card: #ffffff;
    --brand-blue: #1b9bd7;
    --brand-navy: #1d3f8f;
    --ink: #3a3a3c;
    --ink-soft: #6a6a6e;
    --bar-dark: #2e2f33;
  }
  * { box-sizing: border-box; margin: 0; padding: 0; }
  html, body { width: 1200px; height: 895px; overflow: hidden; }
  body {
    background: var(--bg);
    font-family: "Montserrat", Arial, sans-serif;
    color: var(--ink);
    position: relative;
  }
  .card {
    position: absolute;
    top: 290px;
    width: 540px;
    height: 310px;
    background: var(--card);
    box-shadow: 0 6px 18px rgba(0,0,0,0.18);
  }
  .card-front { left: 40px; }
  .card-back { left: 620px; display: flex; align-items: center; justify-content: center; }

  .brand { display: flex; align-items: center; gap: 10px; }
  .brand-dot {
    width: 34px; height: 34px; border-radius: 50%;
    background: var(--brand-blue);
  }
  .brand-name {
    font-weight: 700;
    font-size: 26px;
    letter-spacing: 1px;
    text-transform: uppercase;
    color: var(--brand-blue);
  }
  .card-front .brand { position: absolute; left: 36px; top: 40px; }
  .card-back .brand-name { font-size: 30px; }
  .card-back .brand-dot { width: 40px; height: 40px; }

  .person { position: absolute; left: 80px; top: 100px; }
  .person-name {
    font-size: 15px; font-weight: 600; letter-spacing: 1px;
    text-transform: uppercase; color: var(--ink);
  }
  .person-role {
    font-size: 10px; font-weight: 500; letter-spacing: 1.5px;
    text-transform: uppercase; color: var(--ink-soft); margin-top: 3px;
  }

  .contact { position: absolute; font-size: 10px; color: var(--ink-soft); list-style: none; }
  .contact li { display: flex; align-items: flex-start; gap: 7px; margin-bottom: 7px; line-height: 1.35; }
  .contact svg { flex: none; width: 11px; height: 11px; fill: var(--ink-soft); margin-top: 1px; }
  .contact-left { left: 36px; top: 160px; width: 230px; }
  .contact-right { left: 290px; top: 195px; width: 240px; }
  .contact-right li { font-size: 9.5px; }

  .footer-bar {
    position: absolute; left: 36px; right: 36px; bottom: 42px; height: 5px;
    display: flex;
  }
  .footer-bar .accent { flex: 0 0 46%; background: linear-gradient(90deg, var(--brand-navy), var(--brand-blue)); }
  .footer-bar .base { flex: 1; background: var(--bar-dark); }
</style>
</head>
<body>

<section class="card card-front">
  <div class="brand">
    <span class="brand-dot"></span>
    <span class="brand-name">Mendwise Partners</span>
  </div>

  <div class="person">
    <p class="person-name">Karl Varner</p>
    <p class="person-role">General Manager</p>
  </div>

  <ul class="contact contact-left">
    <li>
      <svg viewBox="0 0 12 12"><path d="M6 0a4 4 0 0 0-4 4c0 3 4 8 4 8s4-5 4-8a4 4 0 0 0-4-4zm0 5.5A1.5 1.5 0 1 1 6 2.5a1.5 1.5 0 0 1 0 3z"/></svg>
      <span>Hillcrest Office Park, 47 Bloem Street<br>Kestrel Building, Northbrook 2190</span>
    </li>
    <li>
      <svg viewBox="0 0 12 12"><circle cx="6" cy="6" r="5.5"/></svg>
      <span>www.mendwisepartners-example.co.za</span>
    </li>
  </ul>

  <ul class="contact contact-right">
    <li>
      <svg viewBox="0 0 12 12"><path d="M2.5 0.5l2 2-1 1.5a7 7 0 0 0 4.5 4.5l1.5-1 2 2-1.5 2C5 11 1 7 0.5 2z"/></svg>
      <span>012 555 0147</span>
    </li>
    <li>
      <svg viewBox="0 0 12 12"><rect x="3" y="0.5" width="6" height="11" rx="1"/></svg>
      <span>012 555 0183</span>
    </li>
    <li>
      <svg viewBox="0 0 12 12"><path d="M0 2h12v8H0z M0 2l6 4 6-4" /></svg>
      <span>karl.varner@mendwisepartners-example.co.za</span>
    </li>
  </ul>

  <div class="footer-bar"><span class="accent"></span><span class="base"></span></div>
</section>

<section class="card card-back">
  <div class="brand">
    <span class="brand-dot"></span>
    <span class="brand-name">Mendwise Partners</span>
  </div>
</section>

</body>
</html>
```